Vostrel Holdings Web Design

Vostrel Holdings Limited Shenzhen

This project is a 10 page launch website.
Our client is seeking a contemporary homepage design for a Holdings company. Once we are happy with the homepage design and select designer we will request a secondary page design.

Please see attached company LOGO for an idea of style, it incorporates the traditional Chinese furniture lattice work. The Quillmoor website is one of our clients favorite so we would like to see a similar homepage design to this website.

Use the websites below for reference purpose. The first two are Chinese and the second two are international. We would like to see elements of both but more focus on international design.

http://www.evergrande.com/http://www.brevandgroup.com/pub/default.aspx http://www.quillmoor.com/zh/maldives_resortone/
http://www.vellune-studio.com
http://media-cache-ec0.fotrelix.com/originals/41/a3/90/41a390c1f5b7d2e8a6c4f0b9e3d71a55.jpg

Company Background
VOSTREL HOLDINGS, located in Qianhai, China, is a new real-estate project operator, structuring urban-rural real-estate investment and development, and industrial fund investment. The company also invests in supply chain management and supporting infrastructures. To create new spaces and livable cities Vostrel Holdings develop win-win strategic partnerships with a number of institutions. Currently cooperating with Harrow East Lindcombe, China urban and rural integrated demonstration.

Target Market(s)

B2B property investment. Target market customers are senior level management/decision makers of large corporations. Focusing geographically on the domestic market first and expanding internationally in 2nd and 3rd years.

Industry/Entity Type

Investment

Requirements
Must have
• Since this is a new company, we would like to the website representing growth and power, E.g. like a growing tree.
Should not have
• Low-level vectors such as curency symbols, American dollar.

```html
<!DOCTYPE html>
<html lang="en">
<head>
<meta charset="utf-8">
<title>Vostrel Holdings</title>
<link href="https://fonts.googleapis.com/css2?family=PT+Sans:wght@400;700&display=swap" rel="stylesheet">
<style>
:root{
  --bar:#262428;
  --gold:#b8963e;
  --red:#d0141b;
  --text:#555;
  --nav:#e8e8e8;
  --line:#e4e4e4;
  --white:#fff;
}
*{margin:0;padding:0;box-sizing:border-box}
html,body{width:905px;height:1200px;overflow:hidden;background:var(--white)}
body{position:relative;font-family:'PT Sans',sans-serif;color:var(--text)}
.abs{position:absolute}

/* header */
.site-header{left:0;top:0;width:905px;height:91px;background:var(--bar)}
.brand{left:120px;top:12px;width:90px;text-align:center}
.brand-mark{width:46px;height:46px;border:2px solid var(--gold);border-radius:50%;margin:0 auto 4px}
.brand-name{font-size:10px;color:var(--gold);white-space:nowrap;letter-spacing:.2px}
.contact-phone{left:492px;top:15px;font-size:10px;color:var(--nav);display:flex;align-items:center;gap:6px}
.lang{left:659px;top:14px;font-size:10px;color:var(--nav);display:flex;align-items:center;gap:6px}
.lang-select{background:var(--white);color:#333;padding:2px 5px;width:52px;display:flex;justify-content:space-between;align-items:center;font-size:9px}
.main-nav{left:231px;top:62px;display:flex;gap:17px;font-size:9px;color:var(--nav);text-transform:uppercase;white-space:nowrap}
.main-nav .active{color:var(--white)}
.search{left:616px;top:58px;width:164px;border-bottom:1px solid #555;display:flex;justify-content:space-between;align-items:center;padding-bottom:4px;font-size:9px;color:var(--nav)}

/* hero */
.hero{left:0;top:91px;width:905px;height:408px;background:linear-gradient(180deg,#3f7fd6 0%,#6fa4e0 22%,#3c8b3b 40%,#1f62c4 58%,#2f7ad8 70%,#d9c9a6 85%,#c8b48a 100%)}
.hero-arrow{top:187px;width:38px;height:38px;border-radius:50%;background:rgba(255,255,255,.55);display:flex;align-items:center;justify-content:center}

/* about */
.about-title{left:122px;top:532px;font-size:19.5px;font-weight:400;color:var(--gold);white-space:nowrap}
.about-title strong{font-weight:700}
.gold-rule{left:122px;top:578px;width:62px;height:2px;background:var(--gold)}
.about-text{left:122px;top:596px;width:346px;font-size:10.5px;line-height:15.3px;color:#666;text-align:justify}
.btn{left:122px;top:720px;width:94px;height:31px;border:2px solid var(--gold);border-radius:3px;color:var(--gold);font-size:10.5px;font-weight:700;display:flex;align-items:center;justify-content:center}
.about-photo{left:509px;top:557px;width:274px;height:173px;border:1px solid #ddd;padding:5px;box-shadow:0 4px 6px rgba(0,0,0,.08);background:var(--white)}
.about-photo div{width:100%;height:100%;background:linear-gradient(180deg,#6f9fd8 0%,#a8c8e8 45%,#e9eef2 55%,#5f8d3a 80%,#4f7d2e 100%)}
.divider{left:120px;top:784px;width:665px;height:4px;background:radial-gradient(ellipse at center,rgba(0,0,0,.1) 0%,rgba(0,0,0,0) 70%)}

/* panels */
.panel-head{top:821px;height:22px;border-bottom:2px solid var(--gold);display:flex}
.tab{height:20px;padding:0 7px;font-size:13px;color:var(--white);background:var(--gold);display:flex;align-items:center}
.tab.muted{background:#8a8a8a}
.news-tile{background:#8aa9c6;overflow:hidden}
.date{width:40px;height:40px;border-radius:50%;background:var(--red);color:var(--white);font-size:10px;font-weight:700;line-height:11px;display:flex;flex-direction:column;align-items:center;justify-content:center;border:2px solid rgba(255,255,255,.6)}
.caption{left:8px;display:flex;flex-direction:column;align-items:flex-start;gap:3px}
.caption span{background:rgba(30,30,30,.85);color:var(--white);font-size:10.5px;padding:2px 5px;text-transform:uppercase;white-space:nowrap}

.city-bar{left:466px;top:853px;width:316px;height:16px;display:flex;align-items:center;font-size:9px}
.on-sale{background:var(--red);color:var(--white);padding:0 6px;height:16px;display:flex;align-items:center;font-weight:700}
.cities{margin-left:4px;flex:1;height:16px;border:1px solid #ccc;display:flex;align-items:center;gap:11px;padding:0 8px;color:#aaa;text-transform:uppercase}
.cities .current{color:#333}
.project{left:466px;width:316px;display:flex;gap:10px}
.project-photo{width:117px;height:72px;flex:none}
.project h3{font-size:10.5px;font-weight:400;color:var(--red);margin-bottom:3px}
.project p{font-size:9.5px;line-height:12.5px;color:#666}
.project .tel{color:var(--red);margin-top:5px}
.sep{left:466px;width:316px;height:1px;background:var(--line)}

/* footer */
.site-footer{left:0;top:1109px;width:905px;height:91px;background:var(--bar)}
.footer-nav{left:122px;display:flex;gap:18px;font-size:10px;color:var(--nav)}
.copyright{left:122px;font-size:9.5px;color:#999}
.follow{left:629px;display:flex;align-items:center;gap:6px;font-size:10px;color:#aaa}
.social{width:22px;height:22px}
</style>
</head>
<body>

<header class="site-header abs">
  <div class="brand abs">
    <div class="brand-mark"></div>
    <div class="brand-name">VOSTREL HOLDINGS</div>
  </div>
  <div class="contact-phone abs">
    <svg width="11" height="11" viewBox="0 0 24 24"><path fill="#e8e8e8" d="M6.6 10.8a15 15 0 0 0 6.6 6.6l2.2-2.2c.3-.3.7-.4 1-.2 1.1.4 2.3.6 3.6.6.6 0 1 .4 1 1V20c0 .6-.4 1-1 1A17 17 0 0 1 3 4c0-.6.4-1 1-1h3.5c.6 0 1 .4 1 1 0 1.3.2 2.5.6 3.6.1.3 0 .7-.2 1z"/></svg>
    (01) 555-246-8013
  </div>
  <div class="lang abs">Select Language:
    <div class="lang-select">English
      <svg width="7" height="5" viewBox="0 0 7 5"><path d="M0 0l3.5 4L7 0" fill="none" stroke="#333" stroke-width="1.2"/></svg>
    </div>
  </div>
  <nav class="main-nav abs">
    <span class="active">Home</span><span>About Us</span><span>News Center</span><span>Vostrel Projects</span><span>Join Us</span><span>Contact</span>
  </nav>
  <div class="search abs">Search
    <svg width="13" height="13" viewBox="0 0 13 13"><circle cx="5.5" cy="5.5" r="4.2" fill="none" stroke="#fff" stroke-width="1.8"/><path d="M8.6 8.6L12 12" stroke="#fff" stroke-width="2"/></svg>
  </div>
</header>

<section class="hero abs" role="img" aria-label="Resort swimming pool lined with palm trees and sun loungers">
  <div class="hero-arrow abs" style="left:121px"><svg width="14" height="14" viewBox="0 0 14 14"><path d="M9 2L4 7l5 5" fill="none" stroke="#fff" stroke-width="2.4"/></svg></div>
  <div class="hero-arrow abs" style="left:744px"><svg width="14" height="14" viewBox="0 0 14 14"><path d="M5 2l5 5-5 5" fill="none" stroke="#fff" stroke-width="2.4"/></svg></div>
</section>

<section class="about">
  <h1 class="about-title abs">About <strong>Vostrel Holdings Limited Shenzhen</strong></h1>
  <div class="gold-rule abs"></div>
  <p class="about-text abs">Lorem ipsum dolor sit amet consectetur adipisicing elit sed do eiusmod tempor incididunt ut labore et dolore magna aliqua. Ut enim ad minim veniam, quis nostrud exercitation ullamco laboris nisi ut aliquip commodo consequat. Duis aute irure dolor in reprehenderit in voluptate velit esse cillum dolore eu fugiat nulla pariatur. Excepteur sint occaecat cupidatat non proident, sunt in culpa qui officia deserunt mollit anim id est laborum.</p>
  <a class="btn abs">READ MORE</a>
  <figure class="about-photo abs"><div role="img" aria-label="White two-storey house on a green lawn under blue sky"></div></figure>
  <div class="divider abs"></div>
</section>

<section class="news">
  <div class="panel-head abs" style="left:121px;width:317px"><span class="tab">Latest News</span></div>
  <article class="news-tile abs" style="left:121px;top:853px;width:161px;height:207px;background:linear-gradient(180deg,#6e9fd6 0%,#cfe0ef 35%,#7d9a6e 60%,#4d7a3a 100%)" role="img" aria-label="City skyline by green hills">
    <div class="date abs" style="left:7px;top:7px">17<br>DEC</div>
    <div class="caption abs" style="top:164px"><span>Lorem ipsum dolor sit</span><span>amet consectetur</span></div>
  </article>
  <article class="news-tile abs" style="left:288px;top:853px;width:150px;height:99px;background:linear-gradient(180deg,#5f97d8 0%,#b7cfe4 45%,#7a8e96 100%)" role="img" aria-label="Tall hotel towers">
    <div class="date abs" style="left:8px;top:7px">17<br>DEC</div>
    <div class="caption abs" style="top:59px"><span>Lorem ipsum dolor sit</span><span>amet consectetur</span></div>
  </article>
  <article class="news-tile abs" style="left:288px;top:960px;width:150px;height:100px;background:linear-gradient(180deg,#8a5a1e 0%,#d9a844 50%,#f0d27a 100%)" role="img" aria-label="Warmly lit hotel lobby">
    <div class="date abs" style="left:8px;top:7px">17<br>DEC</div>
    <div class="caption abs" style="top:60px"><span>Lorem ipsum dolor sit</span><span>amet consectetur</span></div>
  </article>
</section>

<section class="projects">
  <div class="panel-head abs" style="left:466px;width:316px"><span class="tab">Projects</span><span class="tab muted">Map</span></div>
  <div class="city-bar abs">
    <span class="on-sale">ON SALE</span>
    <div class="cities"><span class="current">Shanghai</span><span>Beijing</span><span>Hangzhou</span><span>Wuhan</span><span>Tianjing</span>
      <svg style="margin-left:auto" width="6" height="8" viewBox="0 0 6 8"><path d="M1 1l3 3-3 3" fill="none" stroke="#333" stroke-width="1.4"/></svg></div>
  </div>
  <article class="project abs" style="top:883px">
    <div class="project-photo" style="background:linear-gradient(180deg,#1a1f5a 0%,#3a3f8a 55%,#c07a4a 100%)" role="img" aria-label="City skyline at night"></div>
    <div><h3>Lorem ipsum dolor sit amet consectetur</h3><p>Adipisicing elit sed do eiusmod tempor incididunt labore et dolore magna aliqua.</p><p class="tel">555-246-8013</p></div>
  </article>
  <div class="sep abs" style="top:966px"></div>
  <article class="project abs" style="top:978px">
    <div class="project-photo" style="background:linear-gradient(180deg,#4f8fd6 0%,#a9cbec 55%,#3a6a9a 100%)" role="img" aria-label="Harbour skyline by day"></div>
    <div><h3>Lorem ipsum dolor sit amet consectetur</h3><p>Adipisicing elit sed do eiusmod tempor incididunt labore et dolore magna aliqua.</p><p class="tel">555-246-8013</p></div>
  </article>
  <div class="sep abs" style="top:1061px"></div>
</section>

<footer class="site-footer abs">
  <nav class="footer-nav abs" style="top:23px"><span>Home</span><span>About Us</span><span>News Center</span><span>Vostrel Projects</span><span>Join Us</span><span>Contact</span></nav>
  <p class="copyright abs" style="top:53px">Copyright © 2013 Vostrel Holding. All rights reserved.</p>
  <div class="follow abs" style="top:21px">Follow Vostrel Holding on
    <span class="social" style="background:#3b5998"></span>
    <span class="social" style="background:#2aa3e0"></span>
  </div>
</footer>

</body>
</html>
```